Hello!

I need a 4.25x6.87 RVN paperback cover and OWM audiobook square cover with the same design. Title is "7 SIMPLE NOTES FOR A GENTLE VOYAGE: A Departure, Arrival, and Reflection Manual". Book is 75 pages long.

Originally I typed the prompt of, "A man with aviator goggles and a scarf flying an Amanita Muscaria mushroom," into ChatGPT to create something of the idea I had in mind (image attached).

IMPORTANT: "Amanita Muscaria" mushroom is now inconsistent with the "Psilocybin" in the title, so if you go this route, you might want to look up something like "golden teacher psilocybin mushroom" to get a better idea of the kind of mushroom I need in the image.

Back Sleeve Summary:
Do you have a blossoming interest in mushrooms? Looking for a manual that’s less science-y and more practical? In search of something that skips the history and gets straight to what’s relevant? Well, then, here’s a pocket-sized guide of what you need to know to have a good experience. This succinct foundation of knowledge was written by someone who has tripped countless times with various-sized doses. Topics covered include set and setting, tripping with others, expectations, intentions, dosage, and more. If you’re ready to explore, then let’s dive right in.

Author Section (with attached photo):
Brent Halloway earned a B.S. in Kinesiology from the University of Calvenmoor, and has furthered his studies in the fields of psychedelics, psychology, and trauma healing since 2012. He’s been exploring the benefits of psychedelics within himself for equally as long.

• 4.25x6.87 paperback cover (70-75 pages) and OWM audiobook square cover

```html
<!DOCTYPE html>
<html lang="en">
<head>
<meta charset="utf-8">
<title>7 Simple Notes for a Gentle Voyage — Cover Spread</title>
<link rel="stylesheet" href="https://fonts.googleapis.com/css2?family=Bowlby+One&family=Arimo:wght@400&family=Tinos:wght@400&display=swap">
<style>
  :root {
    --stage: #e4e4e4;
    --cover-yellow: #f9c63d;
    --ink: #141414;
    --title-purple: #b23fd6;
    --title-cyan: #37dbe3;
    --title-green: #86f25c;
    --art-magenta: #d93aa4;
    --art-teal: #2aa9c9;
    --art-dark: #1b1530;
    --photo-grey: #8a8a8a;
  }
  * { margin: 0; padding: 0; box-sizing: border-box; }
  html, body { width: 1200px; height: 529px; overflow: hidden; background: var(--stage); }
  .canvas { position: relative; width: 1200px; height: 529px; }

  .cover-spread {
    position: absolute; left: 270px; top: 13px;
    width: 660px; height: 503px;
    background: var(--cover-yellow);
    color: var(--ink);
  }

  /* Back cover */
  .back-summary, .author-bio {
    position: absolute; left: 37px; width: 240px;
    font-family: "Arimo", Arial, sans-serif;
    font-size: 9.6px; line-height: 12.2px;
    text-align: justify;
  }
  .back-summary { top: 82px; }
  .author-photo {
    position: absolute; left: 37px; top: 241px;
    width: 80px; height: 94px;
    border: 2px solid var(--ink);
    background: linear-gradient(160deg, #d8d8d8, var(--photo-grey) 60%, #3a3a3a);
  }
  .author-label {
    position: absolute; left: 124px; top: 306px;
    font-family: "Bowlby One", sans-serif;
    font-size: 12px; line-height: 15px;
  }
  .author-bio { top: 343px; }

  /* Front cover */
  .front { position: absolute; left: 350px; top: 0; width: 310px; height: 503px; text-align: center; }
  .title-main {
    position: absolute; top: 16px; left: 0; width: 100%;
    font-family: "Bowlby One", sans-serif; font-size: 23px; line-height: 30px;
    white-space: nowrap;
  }
  .title-joiner {
    position: absolute; top: 52px; left: 0; width: 100%;
    font-family: "Bowlby One", sans-serif; font-size: 15px; line-height: 20px;
  }
  .title-highlight {
    position: absolute; top: 76px; left: 0; width: 100%;
    font-family: "Bowlby One", sans-serif; font-size: 25px; line-height: 34px;
    color: var(--title-purple);
    white-space: nowrap;
    -webkit-text-stroke: 0.6px var(--title-cyan);
    text-shadow: -2px -2px 0 var(--title-green), 1px 1px 0 var(--title-cyan);
  }
  .cover-art {
    position: absolute; left: 8px; top: 118px;
    width: 294px; height: 284px;
  }
  .subtitle {
    position: absolute; top: 412px; left: 0; width: 100%;
    font-family: "Tinos", "Times New Roman", serif;
    font-size: 12.5px; line-height: 15px; text-transform: uppercase;
  }
  .author-name {
    position: absolute; top: 455px; left: 0; width: 100%;
    font-family: "Bowlby One", sans-serif; font-size: 18px; line-height: 26px;
    color: var(--title-purple);
    white-space: nowrap;
    -webkit-text-stroke: 0.5px var(--title-cyan);
    text-shadow: -1.5px -1.5px 0 var(--title-cyan);
  }
</style>
</head>
<body>
<main class="canvas">
  <section class="cover-spread">
    <p class="back-summary">Do you have a blossoming interest in mushrooms? Looking for a manual that’s less science-y and more practical? In search of something that skips the history and gets straight to what’s relevant? Well, then, here’s a pocket-sized guide of what you need to know to have a good experience. This succinct foundation of knowledge was written by someone who has tripped countless times with various-sized doses. Topics covered include set and setting, tripping with others, expectations, intentions, dosage, and more. If you’re ready to explore, then let’s dive right in.</p>

    <div class="author-photo" role="img" aria-label="Black and white portrait photo of the author seated"></div>
    <p class="author-label">BRENT<br>HALLOWAY</p>
    <p class="author-bio">earned a B.S. in Kinesiology from the University of Calvenmoor, and has furthered his studies in the fields of psychedelics, psychology, and trauma healing since 2012. He’s been exploring the benefits of psychedelics within himself for equally as long.</p>

    <div class="front">
      <h1 class="title-main">7 SIMPLE NOTES</h1>
      <p class="title-joiner">FOR A</p>
      <p class="title-highlight">GENTLE VOYAGE</p>

      <svg class="cover-art" viewBox="0 0 294 284" role="img" aria-label="Illustration of a hand holding a pink spotted mushroom amid neon rays, seen through torn yellow paper">
        <defs>
          <radialGradient id="art-fill" cx="50%" cy="48%" r="55%">
            <stop offset="0%" stop-color="var(--art-magenta)"/>
            <stop offset="45%" stop-color="var(--art-teal)"/>
            <stop offset="75%" stop-color="var(--art-dark)"/>
            <stop offset="100%" stop-color="#e8c252"/>
          </radialGradient>
        </defs>
        <ellipse cx="147" cy="142" rx="140" ry="136" fill="url(#art-fill)"/>
      </svg>

      <p class="subtitle">A departure, arrival,<br>and reflection manual</p>
      <p class="author-name">BRENT HALLOWAY</p>
    </div>
  </section>
</main>
</body>
</html>
```